Wheels for Harborline Website Design

We need a NEW design and uploaded to Hostavero.com. Here is the current site: http://www.wheelsforharborline.org

Need a form like this:

https://brightlanegifts.org/

```html
<!DOCTYPE html>
<html lang="en">
<head>
<meta charset="utf-8">
<title>Bright Lane Kids – Donate a Car</title>
<link href="https://fonts.googleapis.com/css2?family=Roboto+Condensed:wght@400;700&family=Montserrat:wght@400;500&display=swap" rel="stylesheet">
<style>
:root{
  --blue:#0a4a8c;
  --blue-dark:#073a70;
  --ink:#3a3a3a;
  --muted:#555;
  --line:#c9c9c9;
  --footer:#222222;
  --white:#ffffff;
}
*{box-sizing:border-box;margin:0;padding:0}
html,body{width:1200px;height:3109px;overflow:hidden;background:var(--white)}
body{position:relative;font-family:'Montserrat',sans-serif;color:var(--ink)}
.abs{position:absolute}
.cond{font-family:'Roboto Condensed',sans-serif}
.heading{font-family:'Roboto Condensed',sans-serif;font-weight:700;color:var(--blue);text-transform:uppercase;line-height:1.2}
.body-copy{font-size:12px;line-height:22px;color:var(--muted);text-align:justify}
.btn{position:absolute;background:var(--blue);color:var(--white);font-family:'Roboto Condensed',sans-serif;font-weight:700;font-size:13px;text-transform:uppercase;display:flex;align-items:center;justify-content:center}

/* header */
.brand{display:flex;align-items:center;gap:10px}
.brand-dot{width:34px;height:34px;border-radius:50%;background:var(--blue)}
.brand-name{font-family:'Roboto Condensed',sans-serif;font-weight:700;font-size:22px;line-height:22px;color:var(--blue);text-transform:uppercase}
.main-nav{left:549px;top:146px;display:flex;gap:16px;font-family:'Roboto Condensed',sans-serif;font-size:12px;color:#333;text-transform:uppercase}

/* hero */
.hero-photo{left:103px;top:200px;width:995px;height:480px;background:linear-gradient(180deg,#8fa46a 0%,#7d9152 35%,#9a9a92 70%,#7c7f80 100%)}
.form-card{left:245px;top:261px;width:433px;height:332px;background:var(--white);box-shadow:0 2px 8px rgba(0,0,0,.15)}
.tabs{display:flex;height:73px;border-bottom:1px solid var(--line)}
.tab{flex:1;display:flex;flex-direction:column;align-items:center;justify-content:flex-end;padding-bottom:10px;gap:8px;font-family:'Roboto Condensed',sans-serif;font-size:11px;color:#333;border-left:1px solid var(--line)}
.tab:first-child{border-left:0}
.tab.is-active{background:var(--blue);color:var(--white)}
.form-label{font-family:'Roboto Condensed',sans-serif;font-size:15px;color:#333}
.select{position:absolute;width:124px;height:36px;border:1px solid #bbb;font-size:11px;color:#333;display:flex;align-items:center;padding-left:8px}
.select::after{content:"";position:absolute;right:12px;top:12px;width:6px;height:6px;border-right:1.5px solid #333;border-bottom:1.5px solid #333;transform:rotate(45deg)}

/* how it works */
.step{position:absolute;width:170px;height:170px;border-radius:50%;background:var(--white);box-shadow:0 2px 10px rgba(0,0,0,.12);display:flex;align-items:center;justify-content:center}
.step-ring{width:150px;height:150px;border-radius:50%;border:3px solid var(--blue);display:flex;flex-direction:column;align-items:center;justify-content:center;gap:6px;font-family:'Montserrat',sans-serif;font-weight:500;font-size:14px;color:var(--blue);text-align:center;line-height:18px}
.step.is-filled .step-ring{background:var(--blue);color:var(--white);border-color:var(--blue)}
.step-text{position:absolute;width:220px;font-size:11px;line-height:19px;color:var(--muted);text-align:center}

/* faq */
.faq-item{position:absolute;left:245px;width:376px;height:32px;border:1px solid #aaa;display:flex;align-items:center;font-size:12px;color:#333}
.faq-toggle{width:24px;height:24px;margin:0 10px 0 3px;background:#6c6c6c;color:var(--white);display:flex;align-items:center;justify-content:center;font-size:16px}
.faq-item.is-open{background:var(--blue);border-color:var(--blue);color:var(--white)}
.faq-item.is-open .faq-toggle{background:var(--white);color:var(--blue)}

/* footer */
.footer-title{font-family:'Roboto Condensed',sans-serif;font-weight:700;font-size:18px;color:var(--white);text-transform:uppercase}
.footer-links{font-family:'Roboto Condensed',sans-serif;font-size:12px;color:var(--white);line-height:24px;text-transform:uppercase;list-style:none}
.social{list-style:none;font-family:'Roboto Condensed',sans-serif;font-size:12px;color:var(--white);text-transform:uppercase}
.social li{display:flex;align-items:center;gap:12px;height:32px}
.social-dot{width:22px;height:22px;border-radius:50%;background:var(--white)}
</style>
</head>
<body>

<header>
  <div class="abs brand" style="left:245px;top:134px">
    <span class="brand-dot"></span>
    <span class="brand-name">Bright Lane<br>Kids</span>
  </div>
  <nav class="abs main-nav">
    <span>Home</span><span>How to Donate</span><span>Why Donate</span><span>FAQ</span><span>About</span>
  </nav>
  <div class="btn" style="left:861px;top:134px;width:93px;height:39px;font-size:11px">Donate a Car</div>
</header>

<section>
  <div class="abs hero-photo" role="img" aria-label="Boy driving a toy pedal car on a country road beside tall grass"></div>
  <svg class="abs" style="left:103px;top:600px" width="995" height="80" viewBox="0 0 995 80">
    <polygon points="0,30 620,50 0,80" fill="var(--blue)"/>
  </svg>
  <div class="abs form-card">
    <div class="tabs">
      <div class="tab is-active" style="flex:0 0 60px">
        <svg width="34" height="22" viewBox="0 0 34 22" fill="none" stroke="currentColor" stroke-width="1.6"><path d="M3 14 L6 6 H28 L31 14 V19 H3Z"/><circle cx="9" cy="14" r="2"/><circle cx="25" cy="14" r="2"/></svg>CARS</div>
      <div class="tab"><svg width="40" height="22" viewBox="0 0 40 22" fill="none" stroke="currentColor" stroke-width="1.6"><rect x="2" y="3" width="24" height="13"/><path d="M26 7 H33 L38 12 V16 H26"/><circle cx="9" cy="18" r="2.5"/><circle cx="31" cy="18" r="2.5"/></svg>RVs</div>
      <div class="tab"><svg width="30" height="26" viewBox="0 0 30 26" fill="none" stroke="currentColor" stroke-width="1.6"><path d="M9 4 H21 V11 H9Z"/><path d="M3 13 H27 L23 21 H7Z"/><path d="M2 24 Q8 21 15 24 T28 24"/></svg>BOATS</div>
      <div class="tab"><svg width="40" height="22" viewBox="0 0 40 22" fill="none" stroke="currentColor" stroke-width="1.6"><circle cx="8" cy="15" r="5.5"/><circle cx="32" cy="15" r="5.5"/><path d="M8 15 L16 7 H26 L32 15"/><path d="M24 4 H29"/></svg>MOTORCYCLE</div>
      <div class="tab"><svg width="30" height="26" viewBox="0 0 30 26" fill="none" stroke="currentColor" stroke-width="1.6"><path d="M5 3 L14 12"/><path d="M12 7 L17 2"/><circle cx="20" cy="20" r="4.5"/><path d="M8 18 H14"/></svg>OTHER</div>
    </div>
    <div class="abs form-label" style="left:16px;top:102px">What kind of car?</div>
    <div class="select" style="left:16px;top:128px">Year</div>
    <div class="select" style="left:153px;top:128px">Make</div>
    <div class="select" style="left:290px;top:128px">Model</div>
    <div class="abs form-label" style="left:16px;top:189px">Mileage</div>
    <div class="abs form-label" style="left:153px;top:189px">Does it run?</div>
    <div class="abs form-label" style="left:290px;top:189px">Have the title?</div>
    <div class="select" style="left:16px;top:215px">Select</div>
    <div class="select" style="left:153px;top:215px">Select</div>
    <div class="select" style="left:290px;top:215px">Select</div>
    <div class="btn" style="left:16px;top:266px;width:400px;height:43px;font-size:14px">Donate Now</div>
  </div>
</section>

<section>
  <h2 class="abs heading" style="left:245px;top:750px;font-size:33px;width:360px">Why Donate Your Car to Kids?</h2>
  <p class="abs body-copy" style="left:245px;top:840px;width:362px">Nam libero tempore, cum soluta nobis est eligendi optio cumque nihil impedit quo minus id quod maxime placeat facere possi mus, omnis voluptas assumenda est, omnis dolor repellendus. Temporibus autem quibusdam et aut officiis debitis aut rerum necessitatibus saepe eveniet ut et voluptates repudiandae sint et molestiae non recusandae.</p>
  <div class="btn" style="left:245px;top:992px;width:94px;height:43px">Read More</div>
  <div class="abs" style="left:634px;top:773px;width:464px;height:265px;background:radial-gradient(ellipse at 55% 45%,#c7cacd 0%,#a9adb1 45%,#ffffff 75%)" role="img" aria-label="Silver SUV with branded door decal and a set of car keys"></div>
</section>

<section>
  <div class="abs" style="left:103px;top:1121px;width:995px;height:511px;background:linear-gradient(100deg,#dfe2e7 0%,#eef0f3 35%,#f2f3f5 65%,#dfe2e6 100%)" role="img" aria-label="Soft faded flag backdrop"></div>
  <svg class="abs" style="left:103px;top:1121px" width="995" height="511" viewBox="0 0 995 511">
    <polygon points="500,24 995,2 995,50" fill="var(--blue)"/>
    <polygon points="0,0 995,0 995,2 500,24 0,10" fill="#ffffff"/>
    <polygon points="0,474 500,492 0,511" fill="var(--blue)"/>
    <path d="M101 288 C110 230 140 225 170 218" stroke="var(--blue)" stroke-width="1.8" fill="none" stroke-dasharray="4 4"/>
    <path d="M340 280 C380 300 400 285 420 280" stroke="var(--blue)" stroke-width="1.8" fill="none" stroke-dasharray="4 4"/>
    <path d="M585 228 C620 205 650 215 670 228" stroke="var(--blue)" stroke-width="1.8" fill="none" stroke-dasharray="4 4"/>
    <path d="M832 280 C870 270 890 250 893 222" stroke="var(--blue)" stroke-width="1.8" fill="none" stroke-dasharray="4 4"/>
    <circle cx="101" cy="289" r="6" fill="var(--blue)"/>
    <circle cx="893" cy="220" r="6" fill="var(--blue)"/>
  </svg>
  <h2 class="abs heading" style="left:0;width:1200px;text-align:center;top:1208px;font-size:33px">How It Works</h2>

  <div class="step" style="left:271px;top:1299px"><div class="step-ring">
    <svg width="54" height="54" viewBox="0 0 54 54" fill="none" stroke="currentColor" stroke-width="2.4" stroke-linejoin="round"><path d="M12 8 L20 6 L24 16 L19 20 Q24 31 34 36 L38 31 L48 35 L46 43 Q40 50 30 45 Q14 37 8 22 Q6 13 12 8Z"/><path d="M32 12 Q40 14 42 22"/><path d="M32 4 Q48 7 50 22"/></svg>
    CONTACT US</div></div>
  <div class="step is-filled" style="left:519px;top:1299px"><div class="step-ring">
    <svg width="54" height="48" viewBox="0 0 54 48" fill="none" stroke="currentColor" stroke-width="2.4"><circle cx="14" cy="12" r="9"/><path d="M14 7 V12 H18"/><path d="M6 24 H30 V38 H6Z"/><path d="M30 28 H40 L46 34 V38 H30"/><circle cx="12" cy="41" r="3.5"/><circle cx="38" cy="41" r="3.5"/></svg>
    SCHEDULE<br>PICKUP</div></div>
  <div class="step" style="left:764px;top:1299px"><div class="step-ring">
    <svg width="50" height="50" viewBox="0 0 50 50" fill="none" stroke="currentColor" stroke-width="2.4"><path d="M8 4 H32 V44 H8Z"/><path d="M14 12 H26 M14 20 H26 M14 28 H22"/><path d="M32 22 H40 Q44 22 44 27 V40 Q44 46 38 46 H14"/></svg>
    TAX<br>DEDUCTION</div></div>

  <p class="step-text" style="left:246px;top:1492px">At vero eos et accusamus et iusto odio dig nissimos ducimus qui blanditiis praesentium.</p>
  <p class="step-text" style="left:494px;top:1492px">At vero eos et accusamus et iusto odio dig nissimos ducimus qui blanditiis praesentium.</p>
  <p class="step-text" style="left:739px;top:1492px">At vero eos et accusamus et iusto odio dig nissimos ducimus qui blanditiis praesentium.</p>
</section>

<section>
  <div class="abs" style="left:103px;top:1636px;width:995px;height:513px;background:linear-gradient(90deg,#6c6a5e 0%,#8a8778 35%,#c9ccd0 50%,#f4f5f7 62%,#ffffff 100%)" role="img" aria-label="Smiling soldier in uniform sitting with his two children"></div>
  <h2 class="abs heading" style="left:594px;top:1728px;font-size:33px">Help Us Reach Our Goal</h2>
  <p class="abs cond" style="left:594px;top:1776px;width:370px;font-size:15px;line-height:21px;color:var(--blue)">If you're unsure if we can accept your vehicle, please give us a call at 1800-555-0142.</p>
  <p class="abs body-copy" style="left:594px;top:1831px;width:362px">Nam libero tempore, cum soluta nobis est eligendi optio cumque nihil impedit quo minus id quod maxime placeat facere possi mus, omnis voluptas assumenda est, omnis dolor repellendus. Temporibus autem quibusdam et aut officiis debitis aut rerum necessitatibus saepe eveniet ut et voluptates repudiandae sint et molestiae non recusandae.</p>
  <div class="btn" style="left:594px;top:1984px;width:94px;height:43px">Read More</div>
</section>

<section>
  <h2 class="abs heading" style="left:245px;top:2237px;font-size:33px">Frequently Asked Questions</h2>
  <div class="faq-item is-open" style="top:2305px"><span class="faq-toggle">-</span>What types of vehicles can be donated?
    <svg style="position:absolute;right:12px" width="12" height="8" viewBox="0 0 12 8"><path d="M1 1 L6 6 L11 1" stroke="#fff" stroke-width="1.6" fill="none"/></svg></div>
  <p class="abs" style="left:245px;top:2352px;width:380px;font-size:12px;line-height:19px;color:#333">Nam libero tempore, cum soluta nobis est eligendi optio cumque nihil impedit quo minus id quod maxime placeat facere possimus cum soluta nobis.</p>
  <div class="faq-item" style="top:2424px"><span class="faq-toggle">+</span>What paperwork do I need to donate my vehicle?</div>
  <div class="faq-item" style="top:2467px"><span class="faq-toggle">+</span>Is my donated vehicle tax-deductible?</div>
  <div class="faq-item" style="top:2511px"><span class="faq-toggle">+</span>What if the vehicle is not registered in my name?</div>
  <div class="faq-item" style="top:2554px"><span class="faq-toggle">+</span>When will I receive my tax receipt?</div>
  <div class="abs" style="left:688px;top:2191px;width:410px;height:460px;background:radial-gradient(ellipse at 55% 55%,#5d6244 0%,#7a7458 40%,#c9c6bd 62%,#ffffff 78%)" role="img" aria-label="Child hugging a soldier while holding a small flag"></div>
</section>

<footer>
  <svg class="abs" style="left:103px;top:2635px" width="995" height="368" viewBox="0 0 995 368">
    <polygon points="0,2 500,22 995,42 995,368 0,368" fill="var(--footer)"/>
    <polygon points="500,22 995,6 995,42" fill="var(--blue)"/>
  </svg>
  <div class="abs brand" style="left:245px;top:2700px">
    <span class="brand-dot" style="background:#fff"></span>
    <span class="brand-name" style="color:#fff">Bright Lane<br>Kids</span>
  </div>
  <p class="abs body-copy" style="left:245px;top:2772px;width:280px;color:#ddd">Nemo enim ipsam voluptatem quia voluptas sit aspernatur aut odit aut fugit, sed quia consequun tur magni dolores eos qui ratione voluptatem sequi nesciunt. Neque porro quisquam est, qui do lorem ipsum quia dolor sit amet.</p>
  <h3 class="abs footer-title" style="left:584px;top:2708px">Quick Links</h3>
  <ul class="abs footer-links" style="left:584px;top:2743px"><li>Home</li><li>How to Donate</li><li>Why Donate</li><li>FAQ</li><li>About</li></ul>
  <ul class="abs footer-links" style="left:702px;top:2743px"><li>Blog</li><li>Contact Us</li></ul>
  <h3 class="abs footer-title" style="left:843px;top:2708px">Social Media</h3>
  <ul class="abs social" style="left:843px;top:2740px">
    <li><span class="social-dot"></span>Kinwharf</li>
    <li><span class="social-dot"></span>Vidlantern</li>
    <li><span class="social-dot"></span>Quipsparrow</li>
    <li><span class="social-dot"></span>Boardmeadow</li>
  </ul>
  <div class="abs" style="left:245px;top:2933px;width:709px;height:1px;background:#777"></div>
  <p class="abs cond" style="left:0;width:1200px;text-align:center;top:2958px;font-size:12px;color:#fff">Copyrights @ 2020 Bright Lane Kids. All Rights Reserved.</p>
</footer>

</body>
</html>
```